Redesign Website - Current one too plain

The description is in the uploaded file. Please let me know if you need any more information. I'd prefer it if someone could implement the design to a WordPress site but the best design will win, regardless.
I would like the forms to look nice as well
UPDATE:
I don't think we can use the images that I provided, I think they make the site look a bit 'cheap' and I really don't know how to replace them. One thought I have had is to make the "Simple, Unique, Effective" a second feature on the right side of the page with the search on the left
Target Market(s)
Small companies, private sellers of cars and people who rent their caravan/holiday home out
Industry/Entity Type
Advertising
Number of Pages Required
3 page
Colors
Designer to choose colors to be used in the design.
Look and feel

```html
<!DOCTYPE html>
<html lang="en">
<head>
<meta charset="utf-8">
<title>KARVO – Create Your Advert</title>
<link href="https://fonts.googleapis.com/css2?family=Outfit:wght@300;400;500;600;700&display=swap" rel="stylesheet">
<style>
  :root {
    --ink: #111111;
    --nav-bg: #121212;
    --accent: #e2f91f;
    --field: #f7f4f4;
    --field-line: #e4e1e1;
    --muted: #a9a6a6;
    --white: #ffffff;
  }
  * { box-sizing: border-box; margin: 0; padding: 0; }
  html, body { width: 990px; height: 1200px; overflow: hidden; background: var(--white); }
  body { font-family: "Outfit", sans-serif; color: var(--ink); position: relative; }

  .site-nav {
    position: absolute; left: 17px; top: 18px; width: 956px; height: 62px;
    background: var(--nav-bg); border-radius: 14px;
    display: flex; align-items: center; padding: 0 38px 0 43px;
  }
  .brand { display: flex; align-items: center; gap: 8px; color: var(--accent); font-weight: 500; font-size: 19px; letter-spacing: 2px; }
  .brand-dot { width: 14px; height: 14px; border-radius: 50%; background: var(--accent); }
  .nav-links { position: absolute; left: 371px; display: flex; gap: 17px; list-style: none; font-size: 11.5px; font-weight: 500; color: var(--white); }
  .nav-links .active { color: var(--accent); }
  .login-btn {
    margin-left: auto; width: 107px; height: 34px; border: 1px solid var(--white); border-radius: 17px;
    color: var(--white); font-size: 11.5px; font-weight: 500; display: flex; align-items: center; justify-content: center;
  }

  .hero {
    position: absolute; left: 17px; top: 88px; width: 956px; height: 232px; border-radius: 14px;
    background: linear-gradient(100deg, #243222 0%, #3b4a33 30%, #2c2f2e 48%, #8a949a 58%, #3a3a32 72%, #5a5040 100%);
  }

  .advert { position: absolute; left: 133px; top: 340px; width: 724px; }
  .advert h1 { font-size: 26px; font-weight: 400; letter-spacing: -0.3px; }
  .advert h1 strong { font-weight: 700; }

  .perks { display: flex; margin-top: 14px; height: 37px; }
  .perk {
    background: var(--accent); border-radius: 19px; font-size: 11.5px; font-weight: 400;
    display: flex; align-items: center; justify-content: center; position: absolute; top: 50px; height: 37px;
  }
  .perk.one { left: 0; width: 139px; }
  .perk.two { left: 152px; width: 252px; }
  .perk.three { left: 421px; width: 252px; }

  .prompt { position: absolute; top: 105px; font-size: 14px; font-weight: 400; }
  .prompt strong { font-weight: 500; }

  .field {
    position: absolute; left: 0; width: 724px; height: 46px; background: var(--field); border-radius: 10px;
    font-size: 10.5px; color: var(--muted); padding: 14px 29px; font-weight: 300;
  }
  .field.company { top: 137px; }
  .field.town { top: 240px; }
  .field.web { top: 297px; }
  .field.desc { top: 355px; height: 111px; }

  .select-row { position: absolute; top: 203px; left: 0; width: 724px; display: flex; align-items: center; font-size: 12.5px; }
  .select-row .label { font-size: 14px; font-weight: 500; }
  .option { position: absolute; display: flex; align-items: center; gap: 7px; }
  .option .radio { width: 15px; height: 15px; border-radius: 50%; background: var(--field); position: relative; }
  .option.checked .radio::after { content: ""; position: absolute; left: 5px; top: 5px; width: 5px; height: 5px; border-radius: 50%; background: var(--ink); }
  .opt-car { left: 353px; } .opt-company { left: 485px; } .opt-holiday { left: 624px; }

  .count { position: absolute; top: 483px; font-size: 10.5px; font-weight: 500; }
  .upload-title { position: absolute; top: 516px; font-size: 14px; font-weight: 500; }

  .uploads { position: absolute; top: 551px; left: 0; display: flex; gap: 12px; }
  .upload-box {
    width: 172px; height: 173px; background: var(--field); border-radius: 10px;
    display: flex; flex-direction: column; align-items: center; justify-content: center; gap: 6px;
    font-size: 10.5px; text-align: center; line-height: 1.3;
  }
  .upload-box.main { border: 1px solid var(--field-line); }
  .upload-box svg { width: 34px; height: 34px; }

  .submit {
    position: absolute; top: 747px; left: 1px; width: 129px; height: 35px; background: var(--accent);
    border-radius: 18px; display: flex; align-items: center; justify-content: space-between; padding: 0 16px 0 28px;
    font-size: 12px; font-weight: 500;
  }

  .site-footer { position: absolute; top: 1157px; left: 133px; width: 724px; display: flex; justify-content: space-between; font-size: 12px; font-weight: 300; }
  .site-footer strong { font-weight: 700; }
  .site-footer .legal { font-weight: 400; }
</style>
</head>
<body>
  <header class="site-nav">
    <div class="brand"><span class="brand-dot"></span>KARVO</div>
    <ul class="nav-links">
      <li>Home</li><li class="active">Advertise</li><li>Contact</li><li>Register</li>
    </ul>
    <div class="login-btn">LOGIN</div>
  </header>

  <div class="hero" role="img" aria-label="Silver sports car driving on a winding forest road"></div>

  <main class="advert">
    <h1>Create Your <strong>Advert.</strong></h1>
    <div class="perk one">Free To Advertise</div>
    <div class="perk two">Free graphics to print and display</div>
    <div class="perk three">Weatherproof vinyl graphics available</div>

    <p class="prompt"><strong>Login</strong> or <strong>Register</strong> to create your advert</p>

    <div class="field company">Enter Your Company Name, Make/Model Of Car, etc.</div>

    <div class="select-row">
      <span class="label">Select</span>
      <span class="option opt-car"><span class="radio"></span>Car</span>
      <span class="option opt-company checked"><span class="radio"></span>Company</span>
      <span class="option opt-holiday"><span class="radio"></span>Holiday Name</span>
    </div>

    <div class="field town">Enter Town/City, County or Area.</div>
    <div class="field web">Enter Website or Social Media Pages.</div>
    <div class="field desc">Description - Include Price and Contact Details.</div>

    <p class="count">0 of 4000 max characters.</p>
    <h2 class="upload-title">Upload Images</h2>

    <div class="uploads">
      <div class="upload-box main">
        <svg viewBox="0 0 34 34" fill="none" stroke="#111" stroke-width="2" stroke-linecap="round" stroke-linejoin="round"><path d="M18 5H7a3 3 0 0 0-3 3v19a3 3 0 0 0 3 3h19a3 3 0 0 0 3-3V17"/><circle cx="11" cy="13" r="2.5"/><path d="M4 27l8-8c3-3 6 2 9 0l8-6"/><path d="M26 12V3M22 7l4-4 4 4"/></svg>
        <span>*Upload<br>Main Images First</span>
      </div>
      <div class="upload-box"><svg viewBox="0 0 34 34" fill="none" stroke="#111" stroke-width="2" stroke-linecap="round" stroke-linejoin="round"><path d="M18 5H7a3 3 0 0 0-3 3v19a3 3 0 0 0 3 3h19a3 3 0 0 0 3-3V17"/><circle cx="11" cy="13" r="2.5"/><path d="M4 27l8-8c3-3 6 2 9 0l8-6"/><path d="M26 12V3M22 7l4-4 4 4"/></svg></div>
      <div class="upload-box"><svg viewBox="0 0 34 34" fill="none" stroke="#111" stroke-width="2" stroke-linecap="round" stroke-linejoin="round"><path d="M18 5H7a3 3 0 0 0-3 3v19a3 3 0 0 0 3 3h19a3 3 0 0 0 3-3V17"/><circle cx="11" cy="13" r="2.5"/><path d="M4 27l8-8c3-3 6 2 9 0l8-6"/><path d="M26 12V3M22 7l4-4 4 4"/></svg></div>
      <div class="upload-box"><svg viewBox="0 0 34 34" fill="none" stroke="#111" stroke-width="2" stroke-linecap="round" stroke-linejoin="round"><path d="M18 5H7a3 3 0 0 0-3 3v19a3 3 0 0 0 3 3h19a3 3 0 0 0 3-3V17"/><circle cx="11" cy="13" r="2.5"/><path d="M4 27l8-8c3-3 6 2 9 0l8-6"/><path d="M26 12V3M22 7l4-4 4 4"/></svg></div>
    </div>

    <div class="submit">Submit
      <svg width="15" height="12" viewBox="0 0 15 12" fill="none" stroke="#111" stroke-width="1.6" stroke-linecap="round" stroke-linejoin="round"><path d="M1 6h13M9 1l5 5-5 5"/></svg>
    </div>
  </main>

  <footer class="site-footer">
    <span>© 2023 <strong>KARVO.</strong> All rights reserved.</span>
    <span class="legal">Terms &amp; Conditions &nbsp;|&nbsp; Privacy Policy</span>
  </footer>
</body>
</html>
```